Natural Skin Care e commerce website

we are the distributor for natural skincare product , we would like to develop a e commerce website which encompass the ability to divide the product into face, body , baby , and base on ingredient , best seller, we are Verdel certified product the key point to focus is natural organic , no nasties, vegan , unpolluted , full of natural ingredient. manuka, olive nordic style temporary style website is preferred. the website name is Kolbavi store.co , the web must have ability to take the order and let the brand upload their products

```html
<!DOCTYPE html>
<html lang="en">
<head>
<meta charset="utf-8">
<title>Kolbavi store.co — Natural Skin Care</title>
<link href="https://fonts.googleapis.com/css2?family=Roboto:ital,wght@0,400;0,500;0,700;0,900;1,400&family=Lora:ital@1&display=swap" rel="stylesheet">
<style>
:root{
  --ink:#111111;
  --orange:#FF4500;
  --peach:#FBBF8E;
  --peach-light:#FCDDBF;
  --sky:#C0EBF8;
  --pink:#FB8BBE;
  --charcoal:#333333;
  --star:#FFB800;
  --muted:#8a8a8a;
  --white:#ffffff;
}
*{box-sizing:border-box;margin:0;padding:0}
html,body{width:1200px;height:2775px;overflow:hidden}
body{position:relative;background:var(--white);font-family:'Roboto',sans-serif;color:var(--ink)}
.abs{position:absolute}

/* header */
.site-header{position:absolute;left:0;top:0;width:1200px;height:81px}
.brand{position:absolute;left:0;width:1200px;top:8px;text-align:center;font-weight:900;font-size:38px;letter-spacing:-0.5px}
.header-rule{position:absolute;left:151px;width:899px;height:1px;background:#999}
.main-nav{position:absolute;top:64px;left:0;width:1200px;display:flex;justify-content:center;gap:24px;font-size:9px;letter-spacing:.3px}
.header-icon{position:absolute;top:14px}
.cart-badge{position:absolute;left:1036px;top:36px;width:13px;height:13px;border-radius:50%;background:var(--orange);color:#fff;font-size:8px;font-weight:700;text-align:center;line-height:13px}

/* hero */
.hero{position:absolute;left:0;top:81px;width:1200px;height:524px;background:var(--peach)}
.hero-title{position:absolute;left:155px;width:500px;top:168px;text-align:center;font-size:36px;font-weight:500;line-height:58px}
.btn{display:flex;align-items:center;justify-content:center;font-weight:700;color:#fff;background:var(--orange)}
.hero-btn{position:absolute;top:301px;width:194px;height:44px;border-radius:4px;font-size:16px}
.btn-ghost{background:transparent;border:2px solid #fff}
.hero-photo{position:absolute;left:652px;top:118px;width:548px;height:406px;background:linear-gradient(180deg,#e3b79c 0%,#e9dcd8 55%,#f1ecec 100%)}
.dots{position:absolute;top:494px;left:569px;display:flex;gap:8px}
.dot{width:15px;height:15px;border-radius:50%;border:1.5px solid #111}
.dot.active{background:#111}

/* tabs */
.category-tabs{position:absolute;top:634px;left:0;width:1200px;display:flex;justify-content:center;gap:54px;font-size:20px}
.category-tabs .active{font-weight:700}

/* products */
.product{position:absolute;width:200px;display:flex;flex-direction:column;align-items:center}
.media-slot{height:189px;display:flex;align-items:center;justify-content:center}
.ph-jar{width:176px;height:140px;background:linear-gradient(180deg,#ececec 0%,#fafafa 35%,#dcdcdc 100%)}
.ph-bottle{width:80px;height:189px;background:linear-gradient(180deg,#e9cf86 0%,#d9ae4c 100%)}
.ph-pump{width:136px;height:189px;background:linear-gradient(90deg,#f7f5f2 0%,#efe4d2 100%)}
.p-name{font-size:18px;line-height:24px}
.stars{display:flex;gap:2px;height:18px}
.price{font-size:18px;font-weight:500;line-height:22px}
.cart-btn{width:150px;height:34px;font-size:11px}

/* features */
.feature{position:absolute;width:140px;text-align:center;font-size:11.5px;line-height:18px;text-transform:uppercase}
.feature svg{display:block;margin:0 auto 14px}

/* values */
.values{position:absolute;left:0;top:1192px;width:1200px;height:266px;background:var(--peach-light)}
.values-title{position:absolute;top:30px;left:0;width:1200px;text-align:center;font-size:22px;font-weight:500;line-height:34px}
.value{position:absolute;width:190px;text-align:center;font-size:18px;line-height:27px}
.value svg{display:block;margin:0 auto 6px}

.section-title{position:absolute;left:0;width:1200px;text-align:center;font-size:18px;font-weight:700}

/* testimonials */
.testimonials{position:absolute;left:0;top:1898px;width:1200px;height:315px;background:var(--sky)}
.t-title{position:absolute;top:34px;width:1200px;text-align:center;font-size:22px;font-weight:500}
.t-title span{color:var(--orange)}
.quote-text{position:absolute;left:388px;width:424px;top:86px;text-align:center;font-family:'Lora',serif;font-style:italic;font-size:15px;line-height:26.5px}
.qmark{position:absolute;font-family:'Roboto',sans-serif;font-weight:900;font-size:110px;color:#8a8a8a;line-height:1}
.avatar{position:absolute;border-radius:50%;background:linear-gradient(180deg,#c9b8ae,#8f8079)}
.t-name{position:absolute;font-weight:700}

/* signup */
.signup{position:absolute;left:0;top:2213px;width:1200px;height:300px;background:var(--pink)}
.signup-title{position:absolute;left:151px;top:64px;color:#fff;font-size:22px;font-weight:500;line-height:45px}
.email-input{position:absolute;left:152px;top:184px;width:299px;height:45px;border:2px solid #fff;color:#fde;font-size:14px;padding:0 16px;display:flex;align-items:center}
.submit{position:absolute;left:480px;top:184px;width:150px;height:45px;font-size:15px;border:2px solid #fff}
.signup-photo{position:absolute;left:657px;top:0;width:450px;height:300px;background:linear-gradient(180deg,#f1e4e7 0%,#d6c0c3 50%,#f8d8e6 100%)}

/* footer */
.site-footer{position:absolute;left:0;top:2513px;width:1200px;height:262px;background:var(--charcoal);color:#fff}
.f-col{position:absolute;top:48px;width:300px;text-align:center}
.f-col h3{font-size:18px;font-weight:700;margin-bottom:12px}
.f-col li{list-style:none;font-size:12px;line-height:22.6px}
.copyright{position:absolute;top:212px;width:1200px;text-align:center;font-size:15px}
</style>
</head>
<body>
<svg width="0" height="0" style="position:absolute">
  <defs>
    <symbol id="star" viewBox="0 0 24 24"><path d="M12 1.5l3.2 6.8 7.3.9-5.4 5 1.4 7.3L12 17.9l-6.5 3.6 1.4-7.3-5.4-5 7.3-.9z" fill="#FFB800"/></symbol>
  </defs>
</svg>

<header class="site-header">
  <div class="brand">Kolbavi</div>
  <svg class="header-icon" style="left:984px" width="24" height="30" viewBox="0 0 24 30" fill="none" stroke="#111" stroke-width="1.4"><circle cx="12" cy="9" r="6"/><path d="M2 29c0-7 4-11 10-11s10 4 10 11z"/></svg>
  <svg class="header-icon" style="left:1024px" width="24" height="30" viewBox="0 0 24 30" fill="none" stroke="#111" stroke-width="1.4"><path d="M3 9h18l-1 20H4z"/><path d="M8 9V6a4 4 0 018 0v3"/></svg>
  <div class="cart-badge">0</div>
  <div class="header-rule" style="top:59px"></div>
  <nav class="main-nav"><span>FACE</span><span>BODY</span><span>BABY</span><span>HAIR</span><span>SAMPLES</span></nav>
  <div class="header-rule" style="top:80px"></div>
</header>

<section class="hero">
  <h1 class="hero-title">THE BEST ANTI-AGING<br>YOU'LL EVER TRY</h1>
  <div class="btn hero-btn" style="left:202px">Buy Now</div>
  <div class="btn hero-btn btn-ghost" style="left:412px">Explore More</div>
  <div class="hero-photo" role="img" aria-label="Photo of three smiling women in white tops"></div>
  <div class="dots"><span class="dot active"></span><span class="dot"></span><span class="dot"></span></div>
</section>

<nav class="category-tabs"><span class="active">FACE</span><span>BODY</span><span>BABY</span><span>HAIR</span></nav>

<!-- face products -->
<div class="product" style="left:138px;top:722px">
  <div class="ph-jar" role="img" aria-label="Product photo of a white face cream jar"></div>
  <div class="p-name" style="margin-top:7px">Face cream</div>
  <div class="stars" style="margin-top:10px"><svg width="18" height="18"><use href="#star"/></svg><svg width="18" height="18"><use href="#star"/></svg><svg width="18" height="18"><use href="#star"/></svg><svg width="18" height="18"><use href="#star"/></svg><svg width="18" height="18"><use href="#star"/></svg></div>
  <div class="price" style="margin-top:9px">20.00 $</div>
  <div class="btn cart-btn" style="margin-top:14px">ADD TO CART</div>
</div>
<div class="product" style="left:377px;top:722px">
  <div class="ph-jar" role="img" aria-label="Product photo of a white face cream jar"></div>
  <div class="p-name" style="margin-top:7px">Face cream</div>
  <div class="stars" style="margin-top:10px"><svg width="18" height="18"><use href="#star"/></svg><svg width="18" height="18"><use href="#star"/></svg><svg width="18" height="18"><use href="#star"/></svg><svg width="18" height="18"><use href="#star"/></svg><svg width="18" height="18"><use href="#star"/></svg></div>
  <div class="price" style="margin-top:9px">20.00 $</div>
  <div class="btn cart-btn" style="margin-top:14px">ADD TO CART</div>
</div>
<div class="product" style="left:618px;top:722px">
  <div class="ph-jar" role="img" aria-label="Product photo of a white face cream jar"></div>
  <div class="p-name" style="margin-top:7px">Face cream</div>
  <div class="stars" style="margin-top:10px"><svg width="18" height="18"><use href="#star"/></svg><svg width="18" height="18"><use href="#star"/></svg><svg width="18" height="18"><use href="#star"/></svg><svg width="18" height="18"><use href="#star"/></svg><svg width="18" height="18"><use href="#star"/></svg></div>
  <div class="price" style="margin-top:9px">20.00 $</div>
  <div class="btn cart-btn" style="margin-top:14px">ADD TO CART</div>
</div>
<div class="product" style="left:859px;top:722px">
  <div class="ph-jar" role="img" aria-label="Product photo of a white face cream jar"></div>
  <div class="p-name" style="margin-top:7px">Face cream</div>
  <div class="stars" style="margin-top:10px"><svg width="18" height="18"><use href="#star"/></svg><svg width="18" height="18"><use href="#star"/></svg><svg width="18" height="18"><use href="#star"/></svg><svg width="18" height="18"><use href="#star"/></svg><svg width="18" height="18"><use href="#star"/></svg></div>
  <div class="price" style="margin-top:9px">20.00 $</div>
  <div class="btn cart-btn" style="margin-top:14px">ADD TO CART</div>
</div>

<!-- service features -->
<div class="feature" style="left:373px;top:1036px">
  <svg width="60" height="60" viewBox="0 0 60 60" fill="none" stroke="#111" stroke-width="1.5"><circle cx="30" cy="30" r="28.5"/><path d="M14 22h22v16H14zM36 27h6l4 5v6H36z"/><circle cx="20" cy="40" r="3"/><circle cx="40" cy="40" r="3"/><path d="M20 29l4 4 7-7"/></svg>
  Free standard<br>delivery on all<br>orders over 49€
</div>
<div class="feature" style="left:530px;top:1036px">
  <svg width="60" height="60" viewBox="0 0 60 60" fill="none" stroke="#111" stroke-width="1.5"><circle cx="30" cy="30" r="28.5"/><path d="M16 22l14-6 14 6v16l-14 6-14-6zM16 22l14 6 14-6M30 28v16M23 19l14 6v6"/></svg>
  Easy returns
</div>
<div class="feature" style="left:687px;top:1036px">
  <svg width="60" height="60" viewBox="0 0 60 60" fill="none" stroke="#111" stroke-width="1.5"><circle cx="30" cy="30" r="28.5"/><path d="M15 28l15-6 15 6v12l-15 6-15-6zM15 28l15 6 15-6M30 34v12"/><circle cx="30" cy="18" r="7"/><path d="M27 18l2 2 4-4"/></svg>
  Check when your<br>package arrives
</div>

<section class="values">
  <h2 class="values-title">What makes us<br>different</h2>
  <div class="value" style="left:232px;top:124px">
    <svg width="54" height="54" viewBox="0 0 54 54" fill="none" stroke="#111" stroke-width="1.5"><circle cx="27" cy="27" r="25.5"/><circle cx="27" cy="27" r="12"/><path d="M15 27h24M27 15c5 5 5 19 0 24M27 15c-5 5-5 19 0 24"/></svg>
    100% Natural Organic<br>Products
  </div>
  <div class="value" style="left:449px;top:124px">
    <svg width="54" height="54" viewBox="0 0 54 54" fill="none" stroke="#111" stroke-width="1.5"><circle cx="27" cy="27" r="25.5"/><g fill="#111" stroke="none"><circle cx="27" cy="14" r="2"/><circle cx="27" cy="40" r="2"/><circle cx="14" cy="27" r="2"/><circle cx="40" cy="27" r="2"/><circle cx="18" cy="18" r="1.6"/><circle cx="36" cy="18" r="1.6"/><circle cx="18" cy="36" r="1.6"/><circle cx="36" cy="36" r="1.6"/></g></svg>
    We are<br>sustainable
  </div>
  <div class="value" style="left:631px;top:124px">
    <svg width="54" height="54" viewBox="0 0 54 54" fill="none" stroke="#111" stroke-width="1.5"><circle cx="27" cy="27" r="25.5"/><path d="M17 17l20 20"/><circle cx="27" cy="27" r="11"/></svg>
    No cruelty to<br>animals
  </div>
  <div class="value" style="left:815px;top:124px">
    <svg width="54" height="54" viewBox="0 0 54 54" fill="none" stroke="#111" stroke-width="1.5"><circle cx="27" cy="27" r="25.5"/><path d="M27 24c-3-6-11-4-9 3 1 4 9 9 9 9s8-5 9-9c2-7-6-9-9-3z"/><path d="M12 30c3 8 9 12 15 12s12-4 15-12"/></svg>
    Advice from<br>experts
  </div>
</section>

<h2 class="section-title" style="top:1489px">THE BEST SELLERS</h2>

<div class="product" style="left:139px;top:1540px">
  <div class="media-slot"><div class="ph-jar" role="img" aria-label="Product photo of a white face cream jar"></div></div>
  <div class="p-name" style="margin-top:10px">Face cream</div>
  <div class="stars" style="margin-top:12px"><svg width="18" height="18"><use href="#star"/></svg><svg width="18" height="18"><use href="#star"/></svg><svg width="18" height="18"><use href="#star"/></svg><svg width="18" height="18"><use href="#star"/></svg><svg width="18" height="18"><use href="#star"/></svg></div>
  <div class="price" style="margin-top:8px">20.00 $</div>
  <div class="btn cart-btn" style="margin-top:13px">ADD TO CART</div>
</div>
<div class="product" style="left:379px;top:1540px">
  <div class="media-slot"><div class="ph-bottle" role="img" aria-label="Product photo of a golden body cream bottle"></div></div>
  <div class="p-name" style="margin-top:10px">Body cream</div>
  <div class="stars" style="margin-top:12px"><svg width="18" height="18"><use href="#star"/></svg><svg width="18" height="18"><use href="#star"/></svg><svg width="18" height="18"><use href="#star"/></svg><svg width="18" height="18"><use href="#star"/></svg><svg width="18" height="18"><use href="#star"/></svg></div>
  <div class="price" style="margin-top:8px">20.00 $</div>
  <div class="btn cart-btn" style="margin-top:13px">ADD TO CART</div>
</div>
<div class="product" style="left:620px;top:1540px">
  <div class="media-slot"><div class="ph-pump" role="img" aria-label="Product photo of a baby cream pump bottle beside its box"></div></div>
  <div class="p-name" style="margin-top:10px">Baby cream</div>
  <div class="stars" style="margin-top:12px"><svg width="18" height="18"><use href="#star"/></svg><svg width="18" height="18"><use href="#star"/></svg><svg width="18" height="18"><use href="#star"/></svg><svg width="18" height="18"><use href="#star"/></svg><svg width="18" height="18"><use href="#star"/></svg></div>
  <div class="price" style="margin-top:8px">20.00 $</div>
  <div class="btn cart-btn" style="margin-top:13px">ADD TO CART</div>
</div>
<div class="product" style="left:862px;top:1540px">
  <div class="media-slot"><div class="ph-bottle" role="img" aria-label="Product photo of a golden body cream bottle"></div></div>
  <div class="p-name" style="margin-top:10px">Body cream</div>
  <div class="stars" style="margin-top:12px"><svg width="18" height="18"><use href="#star"/></svg><svg width="18" height="18"><use href="#star"/></svg><svg width="18" height="18"><use href="#star"/></svg><svg width="18" height="18"><use href="#star"/></svg><svg width="18" height="18"><use href="#star"/></svg></div>
  <div class="price" style="margin-top:8px">20.00 $</div>
  <div class="btn cart-btn" style="margin-top:13px">ADD TO CART</div>
</div>

<section class="testimonials">
  <h2 class="t-title">Join our <span>25.000+</span> happy clients</h2>
  <div class="qmark" style="left:314px;top:74px">“</div>
  <div class="qmark" style="left:836px;top:138px">”</div>
  <p class="quote-text">Lorem ipsum dolor sit amet, consectetur adipiscing elit, sed do eiusmod tempor incididunt ut labore et dolore magna aliqua. Quis ipsum suspendisse ultrices gravida. Risus commodo viverra maecenas accumsan lacus vel facilisis.</p>
  <svg class="abs" style="left:246px;top:110px" width="32" height="56" viewBox="0 0 32 56" fill="none" stroke="#777" stroke-width="2"><path d="M30 2L3 28l27 26"/></svg>
  <svg class="abs" style="left:929px;top:110px" width="32" height="56" viewBox="0 0 32 56" fill="none" stroke="#777" stroke-width="2"><path d="M2 2l27 26L2 54"/></svg>
  <div class="avatar" style="left:189px;top:231px;width:46px;height:46px;opacity:.6" role="img" aria-label="Customer portrait"></div>
  <div class="t-name" style="left:246px;top:247px;font-size:10px;color:var(--muted)">Mira Lenton</div>
  <div class="avatar" style="left:515px;top:221px;width:66px;height:66px" role="img" aria-label="Customer portrait"></div>
  <div class="t-name" style="left:595px;top:245px;font-size:14px">Sofia Varell</div>
  <div class="avatar" style="left:894px;top:231px;width:46px;height:46px;opacity:.6" role="img" aria-label="Customer portrait"></div>
  <div class="t-name" style="left:950px;top:249px;font-size:10px;color:var(--muted)">Nora Ekdahl</div>
</section>

<section class="signup">
  <h2 class="signup-title">SIGN UP FOR EMAILS AND<br>GET IN ON ALL THE ACTION</h2>
  <div class="email-input">Enter your email adress:</div>
  <div class="btn submit">SUBMIT</div>
  <div class="signup-photo" role="img" aria-label="Photo of two friends on a bed with towels on their heads holding skincare products"></div>
</section>

<footer class="site-footer">
  <div class="f-col" style="left:106px"><h3>OUR PRODUCTS</h3><ul><li>FACE</li><li>BODY</li><li>BABY</li><li>HAIR</li><li>SAMPLES</li></ul></div>
  <div class="f-col" style="left:490px"><h3>SECURITY &amp; PRIVACY</h3><ul><li>TERMS OF SERVICE</li><li>DELIVERY AND RETURNS POLICY</li><li>SECURE PAYMENT</li><li>PRIVACY POLICY</li></ul></div>
  <div class="f-col" style="left:833px"><h3>HELP</h3><ul><li>CONTACT</li></ul></div>
  <p class="copyright">© 2020 Kolbavi. All Rights Reserved</p>
</footer>
</body>
</html>
```